Startup Technology Consulting Firm in NYC Needs A Website

I need a website built for my startup technology consulting company Brightmoor Systems Collective. We offer a unique white glove service that provides end to end technology support. I want to stand out above the rest. We are small firm but are very dedicated which where we derive our name from BSC primarily offers
end to end technology advisory services to small businesses lacking their own IT staff. We offer top notch white glove and our customer service and satisfaction is exceed by no one.

Below are some of what we provide our clients

Strategic IT Planning
Business Continuity Planning/Disaster Recovery
Cloud Computing\DataCenter Solutions
Server Infrastructure/Networking
Virtualization Technologies
Project Management

Our Technology Advisors hold many certifications from Quillora & Tessfold. We are also Quillora Partners

I have attached my logo (preview design) As soon as I ge the final images I will upload.

Reason: want to give more time to submit designs

Industry/Entity Type

Information Technology

Coding

Coded - Design and coding required

Number of Pages Required

1 page

Font styles to use
Sans Serif

Requirements
Must have
• Attract Target Market. The site should bleed the company vision
• DEDICATION everything about the site should show this
• Layout the Benefits of our offerings
• Links to my social media
• Links to dircct my client's for remote support

```html
<!DOCTYPE html>
<html lang="en">
<head>
<meta charset="utf-8">
<title>Brightmoor Systems Collective</title>
<link rel="stylesheet" href="https://fonts.googleapis.com/css2?family=Open+Sans:wght@400;600;700;800&display=swap">
<style>
:root{
  --blue:#1d6fb5;
  --navy:#0f4f8c;
  --deep:#0b2f57;
  --sky:#2a8ad8;
  --heading:#1f7ac4;
  --text:#444;
  --muted:#888;
  --line:#dcdcdc;
  --grey:#eeeeef;
  --green:#3a9a2f;
  --red:#d8352a;
  --white:#fff;
}
*{box-sizing:border-box;margin:0;padding:0}
html,body{width:1200px;height:2720px;overflow:hidden}
body{font-family:"Open Sans",Arial,sans-serif;color:var(--text);background:var(--white);position:relative}
.abs{position:absolute}

/* header */
.topbar{left:0;top:0;width:1200px;height:121px;background:var(--white)}
.brand{left:170px;top:62px;display:flex;align-items:center;gap:12px}
.brand-dot{width:44px;height:44px;border-radius:50%;background:var(--blue)}
.brand-name{font-weight:700;font-size:19px;color:var(--blue);line-height:1.15;width:190px}
.social-top{right:84px;top:6px;display:flex;gap:8px}
.social-top span{width:26px;height:26px;border-radius:50%;background:#222}
.contact-item{top:56px;display:flex;gap:10px;font-size:13px}
.contact-item svg{width:18px;height:18px;margin-top:2px}
.contact-item small{display:block;color:var(--muted);font-size:12px}
.contact-item b{color:#222;font-weight:700;font-size:14px}
.navbar{left:400px;top:121px;width:800px;height:36px;background:var(--navy);display:flex;align-items:center;padding-left:20px}
.navbar a{color:var(--white);text-decoration:none;font-size:13px;font-weight:700;margin-right:44px}
.book{left:906px;top:121px;width:124px;height:36px;background:var(--sky);border-radius:18px;color:var(--white);font-size:13px;font-weight:700;display:flex;align-items:center;justify-content:center}
.navline{left:0;top:148px;width:400px;height:9px;background:var(--navy)}

/* hero */
.hero{left:0;top:157px;width:1200px;height:658px;clip-path:polygon(0 0,100% 0,100% 100%,64% 80%,0 78%)}
.hero-photo{position:absolute;inset:0;background:linear-gradient(120deg,#6d87a4 0%,#3e6288 40%,#22476f 70%,#13314f 100%)}
.hero-shade{position:absolute;inset:0;background:rgba(11,47,87,.45)}
.hero-wedge{left:0;top:560px;width:1200px;height:260px}
.hero-title{left:0;top:365px;width:1200px;text-align:center;color:var(--white);font-size:38px;font-weight:600;letter-spacing:1px}
.hero-text{left:200px;top:415px;width:800px;text-align:center;color:var(--white);font-size:19px;line-height:1.45}
.hero-btn{left:470px;top:508px;width:260px;height:60px;border-radius:30px;background:var(--blue);color:var(--white);font-size:22px;font-weight:600;display:flex;align-items:center;justify-content:center;box-shadow:0 4px 10px rgba(0,0,0,.25)}

/* section headings */
.sec-title{left:0;width:1200px;text-align:center;color:var(--heading);font-size:19px;font-weight:700}
.sec-sub{left:0;width:1200px;text-align:center;color:var(--muted);font-size:12px;font-style:italic}
.sec-rule{left:540px;width:120px;height:2px;background:var(--line)}

/* about */
.photo-circle{border-radius:50%;border:5px solid var(--white);box-shadow:0 0 0 1px var(--line),0 3px 8px rgba(0,0,0,.15)}
.feat-title{color:var(--blue);font-size:14px;font-weight:700;text-align:center;width:360px}
.feat-text{color:var(--muted);font-size:12px;line-height:1.5;text-align:center;width:300px}

/* clouds */
.clouds{left:0;top:1200px;width:1200px;height:170px;background:linear-gradient(180deg,#fff 0%,#dcdee2 45%,#e9eaec 75%,var(--grey) 100%)}

/* services */
.services-bg{left:0;top:1360px;width:1200px;height:430px;background:var(--grey);clip-path:polygon(0 0,100% 0,100% 72%,50% 80%,0 100%)}
.svc-card{width:136px;height:120px;background:var(--white);display:flex;align-items:center;justify-content:center;box-shadow:0 1px 3px rgba(0,0,0,.08)}
.svc-card svg{width:48px;height:48px}
.svc-title{font-size:15px;font-weight:700;color:#222;width:170px}
.svc-text{font-size:12px;color:var(--muted);line-height:1.45;width:150px}

/* hosting */
.plan{width:266px;height:323px;background:#f5f5f5;border:1px solid #e6e6e6;text-align:center;overflow:hidden}
.plan svg{width:56px;height:56px;margin-top:38px}
.plan h3{font-size:18px;font-weight:600;color:#222;margin-top:10px}
.plan .tag{font-size:12px;color:var(--muted);margin-top:2px}
.plan .from{font-size:11px;font-weight:700;color:#333;margin-top:22px;letter-spacing:.5px}
.plan .price{font-size:26px;font-weight:700;color:var(--green);margin-top:0}
.plan .btn{width:136px;height:50px;margin:16px auto 0;background:var(--blue);color:var(--white);font-size:15px;font-weight:600;display:flex;align-items:center;justify-content:center;border-radius:2px}
.ribbon{left:-40px;top:26px;width:160px;height:24px;background:var(--red);color:var(--white);font-size:10px;font-weight:700;text-align:center;line-height:24px;transform:rotate(-45deg)}

/* footer */
.footer{left:0;top:2290px;width:1200px;height:430px}
.social-foot{left:0;top:2476px;width:1200px;display:flex;justify-content:center;gap:12px}
.social-foot span{width:40px;height:40px;border-radius:50%;background:var(--white)}
.foot-title{left:0;top:2540px;width:1200px;text-align:center;color:var(--white);font-size:28px;font-weight:700;letter-spacing:1px}
.foot-line{left:0;width:1200px;text-align:center;color:var(--white);font-size:13px}
.foot-rule{left:360px;top:2650px;width:480px;height:1px;background:rgba(255,255,255,.3)}
</style>
</head>
<body>

<header>
  <div class="abs topbar"></div>
  <div class="abs brand"><span class="brand-dot"></span><span class="brand-name">Brightmoor Systems Collective</span></div>
  <div class="abs social-top"><span></span><span></span><span></span><span></span></div>

  <div class="abs contact-item" style="left:483px">
    <svg viewBox="0 0 24 24"><path fill="#1d6fb5" d="M6.6 10.8a15 15 0 006.6 6.6l2.2-2.2a1 1 0 011-.25 11.4 11.4 0 003.6.57 1 1 0 011 1V20a1 1 0 01-1 1A17 17 0 013 4a1 1 0 011-1h3.5a1 1 0 011 1c0 1.25.2 2.45.57 3.6a1 1 0 01-.25 1z"/></svg>
    <div><small>Call Us Anytime</small><b>08-5550-2800</b></div>
  </div>
  <div class="abs contact-item" style="left:670px">
    <svg viewBox="0 0 24 24"><circle cx="12" cy="12" r="9" fill="none" stroke="#1d6fb5" stroke-width="2"/><path d="M12 7v5l3 2" fill="none" stroke="#1d6fb5" stroke-width="2"/></svg>
    <div><small>Opening Time</small><b>08:00 - 18:00</b></div>
  </div>
  <div class="abs contact-item" style="left:840px">
    <svg viewBox="0 0 24 24"><rect x="3" y="6" width="18" height="12" fill="none" stroke="#1d6fb5" stroke-width="2"/><path d="M3 6l9 7 9-7" fill="none" stroke="#1d6fb5" stroke-width="2"/></svg>
    <div><small>Email Us</small><b>info@brightmoorcollective.com</b></div>
  </div>

  <div class="abs navline"></div>
  <nav class="abs navbar">
    <a>HOME</a><a>ABOUT US</a><a>SERVICES</a><a>BLOG</a><a>CONTACT US</a>
  </nav>
  <div class="abs book">BOOKING NOW</div>
</header>

<section>
  <div class="abs hero">
    <div class="hero-photo" role="img" aria-label="Business people at a desk reviewing documents, in blue tones"></div>
    <div class="hero-shade"></div>
  </div>
  <div class="abs hero-title">BRIGHTMOOR SYSTEMS COLLECTIVE</div>
  <div class="abs hero-text">Ut wisi enim ad minim veniam, quis nostrud exerci tation ullamcorper suscipit lobortis nisl ut aliquip ex ea commodo consequat. Duis autem vel eum</div>
  <div class="abs hero-btn">LEARN MORE</div>
</section>

<section>
  <div class="abs sec-title" style="top:766px">ABOUT US</div>
  <div class="abs sec-sub" style="top:794px">Duis autem vel eum iriure dolor in hendrerit in vulputate velit esse molestie consequat</div>
  <div class="abs sec-rule" style="top:815px"></div>

  <div class="abs photo-circle" style="left:234px;top:880px;width:124px;height:124px;background:linear-gradient(135deg,#7a8fa8,#2f4a6b)" role="img" aria-label="Team planning around a laptop"></div>
  <div class="abs photo-circle" style="left:835px;top:880px;width:124px;height:124px;background:linear-gradient(135deg,#c9b8b2,#7a2f35)" role="img" aria-label="Project meeting around a table"></div>
  <div class="abs photo-circle" style="left:513px;top:936px;width:170px;height:170px;background:linear-gradient(160deg,#8d9299,#33363b)" role="img" aria-label="Businessman holding an umbrella in the rain"></div>

  <div class="abs feat-title" style="left:116px;top:1032px">STRATEGIC IT PLANNING</div>
  <div class="abs feat-text" style="left:146px;top:1054px">Ut wisi enim ad minim veniam, quis nostrud exerci tation ullamcorper suscipit lobortis</div>
  <div class="abs feat-title" style="left:717px;top:1032px">PROJECT MANAGEMENT</div>
  <div class="abs feat-text" style="left:747px;top:1054px">Ut wisi enim ad minim veniam, quis nostrud exerci tation ullamcorper suscipit lobortis</div>
  <div class="abs feat-title" style="left:370px;top:1132px;width:460px">BUSINESS CONTINUITY PLANNING/DISASTER RECOVERY</div>
  <div class="abs feat-text" style="left:450px;top:1154px">Ut wisi enim ad minim veniam, quis nostrud exerci tation ullamcorper suscipit lobortis</div>
</section>

<div class="abs clouds" role="img" aria-label="Soft grey clouds band"></div>

<section>
  <div class="abs services-bg"></div>
  <div class="abs sec-title" style="top:1378px">OUR SERVICES</div>
  <div class="abs sec-sub" style="top:1404px">Duis autem vel eum iriure dolor in hendrerit in vulputate velit esse molestie consequat</div>
  <div class="abs sec-rule" style="top:1425px;background:#d2d2d2"></div>

  <div class="abs svc-card" style="left:172px;top:1480px"><svg viewBox="0 0 48 48"><path fill="#1d6fb5" d="M6 19h8l18-9v28l-18-9H6z"/><rect x="12" y="29" width="6" height="10" fill="#1d6fb5"/><path d="M37 18c3 3 3 9 0 12" stroke="#1d6fb5" stroke-width="3" fill="none"/></svg></div>
  <div class="abs svc-card" style="left:405px;top:1480px"><svg viewBox="0 0 48 48"><rect x="6" y="34" width="7" height="8" fill="#1d6fb5"/><rect x="17" y="28" width="7" height="14" fill="#1d6fb5"/><rect x="28" y="22" width="7" height="20" fill="#1d6fb5"/><path d="M8 24L22 14l6 4 12-10" stroke="#1d6fb5" stroke-width="3" fill="none"/><path d="M34 6h8v8z" fill="#1d6fb5"/></svg></div>
  <div class="abs svc-card" style="left:646px;top:1480px"><svg viewBox="0 0 48 48"><path fill="#1d6fb5" d="M6 19h8l18-9v28l-18-9H6z"/><rect x="12" y="29" width="6" height="10" fill="#1d6fb5"/><path d="M37 18c3 3 3 9 0 12" stroke="#1d6fb5" stroke-width="3" fill="none"/></svg></div>
  <div class="abs svc-card" style="left:879px;top:1480px"><svg viewBox="0 0 48 48"><rect x="6" y="34" width="7" height="8" fill="#1d6fb5"/><rect x="17" y="28" width="7" height="14" fill="#1d6fb5"/><rect x="28" y="22" width="7" height="20" fill="#1d6fb5"/><path d="M8 24L22 14l6 4 12-10" stroke="#1d6fb5" stroke-width="3" fill="none"/><path d="M34 6h8v8z" fill="#1d6fb5"/></svg></div>

  <div class="abs svc-title" style="left:172px;top:1610px">Search Engine</div>
  <div class="abs svc-text" style="left:172px;top:1632px">Ut wisi enim ad minim veniam, quis nostrud.</div>
  <div class="abs svc-title" style="left:405px;top:1610px">Search Optimization</div>
  <div class="abs svc-text" style="left:405px;top:1632px">Ut wisi enim ad minim veniam, quis nostrud.</div>
  <div class="abs svc-title" style="left:646px;top:1610px">Search Engine</div>
  <div class="abs svc-text" style="left:646px;top:1632px">Ut wisi enim ad minim veniam, quis nostrud.</div>
  <div class="abs svc-title" style="left:879px;top:1610px">Search Optimization</div>
  <div class="abs svc-text" style="left:879px;top:1632px">Ut wisi enim ad minim veniam, quis nostrud.</div>
</section>

<section>
  <div class="abs sec-title" style="top:1822px">DIFFERENT HOSTING PLATFORMS</div>
  <div class="abs sec-sub" style="top:1849px">Duis autem vel eum iriure dolor in hendrerit in vulputate velit esse molestie consequat</div>
  <div class="abs sec-rule" style="top:1870px"></div>

  <div class="abs plan" style="left:172px;top:1927px">
    <div class="abs ribbon">BEST SELLER</div>
    <svg viewBox="0 0 56 56"><rect x="21" y="4" width="14" height="12" fill="#222"/><path d="M28 16v10M10 26h36M10 26v8M28 26v8M46 26v8" stroke="#222" stroke-width="3" fill="none"/><rect x="3" y="34" width="14" height="12" fill="#222"/><rect x="21" y="34" width="14" height="12" fill="#222"/><rect x="39" y="34" width="14" height="12" fill="#222"/></svg>
    <h3>Web Hosting</h3><div class="tag">The ultimate shared solutions!</div>
    <div class="from">PRICES FROM</div><div class="price">$3.95/mo.</div>
    <div class="btn">Learn More</div>
  </div>
  <div class="abs plan" style="left:468px;top:1927px">
    <svg viewBox="0 0 56 56"><path d="M14 42a10 10 0 01-1-20 14 14 0 0127-3 11 11 0 012 23z" fill="none" stroke="#222" stroke-width="3"/></svg>
    <h3>Cloud Hosting</h3><div class="tag">High performance cloud platform!</div>
    <div class="from">PRICES FROM</div><div class="price">$45.00/mo.</div>
    <div class="btn">Learn More</div>
  </div>
  <div class="abs plan" style="left:764px;top:1927px">
    <svg viewBox="0 0 56 56"><ellipse cx="28" cy="11" rx="17" ry="6" fill="none" stroke="#222" stroke-width="3"/><path d="M11 11v34c0 3.3 7.6 6 17 6s17-2.7 17-6V11M11 23c0 3.3 7.6 6 17 6s17-2.7 17-6M11 34c0 3.3 7.6 6 17 6s17-2.7 17-6" fill="none" stroke="#222" stroke-width="3"/></svg>
    <h3>Dedicated Hosting</h3><div class="tag">Premium fully managed machines!</div>
    <div class="from">PRICES FROM</div><div class="price">$217.50/mo.</div>
    <div class="btn">Learn More</div>
  </div>
</section>

<footer>
  <svg class="abs footer" viewBox="0 0 1200 430" preserveAspectRatio="none">
    <polygon points="0,40 460,110 1200,0 1200,430 0,430" fill="#0f4f8c"/>
    <polygon points="0,120 1200,60 1200,430 0,430" fill="#1a64a8"/>
  </svg>
  <div class="abs social-foot"><span></span><span></span><span></span><span></span><span></span></div>
  <div class="abs foot-title">CONTACT INFORMATION</div>
  <div class="abs foot-line" style="top:2584px">412 Hollin Street, Northvale, NV 2210</div>
  <div class="abs foot-line" style="top:2606px">Telephone: +1 555 013 4470 &nbsp;/&nbsp; FAX: +1 555 017 2286</div>
  <div class="abs foot-rule"></div>
  <div class="abs foot-line" style="top:2672px">© 2015 Brightmoor Systems Collective. &nbsp;/&nbsp; Privacy Policy &nbsp;/&nbsp; All Reserved</div>
</footer>

</body>
</html>
```